K & D A/C Compressors' Business Card

Hello,

I need someone to create a new business card for my business. The name of my Business is: K & D A/C Compressors. I sell automotive air conditioning parts (a/c parts). I would like the business card to incorporate my logo, and to have an automotive feel to it. It is important that the business card feel like it is coming from an automotive parts business.

I already have a logo, which I will provide.

Thanks.
Updates

Project Deadline Extended Reason: I feel like extending the deadline until October 9, 2017, will allow for more time to design the business card. Thank you for your understanding. Added Monday, October 2, 2017

Target Market(s)

Consumers who need automotive a/c parts, and auto mechanics.

Industry/Entity Type

Automotive

Contact Information for Business Card

Business name: K & D A/C Compressors
Business Address: 48207 Southwest 36th Street, Palmetto Grove, Florida 33990
Telephone: 305-472-1390
Fax: To be provided once I choose your design.
Website: www.kdcoolunits.example
Email: support@kdcoolunits.example
Names: To be provided once I choose your design.

Font styles to use
Sans Serif

Colors

Designer to choose colors to be used in the design.

Requirements
Must have
• The business card must include all of the "Business Card Details" and the logo I have uploaded.

```html
<!DOCTYPE html>
<html lang="en">
<head>
<meta charset="utf-8">
<title>K &amp; D A/C Compressors – Business Card</title>
<link rel="stylesheet" href="https://fonts.googleapis.com/css2?family=Montserrat:wght@700&family=Nunito+Sans:wght@300;400;600&display=swap">
<style>
  :root {
    --stage: #1c1d1f;
    --brand-blue: #29abe2;
    --brand-blue-light: #56c0ea;
    --band-grey: #a7a9ac;
    --paper: #ffffff;
    --ink-grey: #8a8c8f;
  }
  * { margin: 0; padding: 0; box-sizing: border-box; }
  html, body { width: 1200px; height: 900px; overflow: hidden; background: var(--stage); }
  body { font-family: "Nunito Sans", Arial, sans-serif; }

  .card {
    position: absolute;
    left: 260px;
    width: 680px;
    height: 388px;
    overflow: hidden;
    box-shadow: 0 12px 30px rgba(0,0,0,.5);
  }
  .card--front { top: 44px; background: var(--brand-blue); }
  .card--back { top: 468px; background: var(--paper); }

  .front-facet { position: absolute; inset: 0; width: 100%; height: 100%; }

  .wordmark {
    position: absolute;
    display: flex;
    align-items: center;
    gap: 14px;
    color: var(--paper);
    font-family: "Nunito Sans", Arial, sans-serif;
    font-weight: 600;
    white-space: nowrap;
  }
  .wordmark__square { background: var(--paper); flex: none; }
  .card--front .wordmark { left: 50%; top: 50%; transform: translate(-50%, -50%); font-size: 40px; }
  .card--front .wordmark__square { width: 30px; height: 30px; }

  .back-band {
    position: absolute;
    left: 0; right: 0;
    top: 150px; height: 196px;
    background: var(--band-grey);
  }
  .card--back .wordmark { right: 34px; top: 168px; font-size: 25px; }
  .card--back .wordmark__square { width: 20px; height: 20px; background: var(--brand-blue); }

  .holder { position: absolute; left: 40px; top: 92px; }
  .holder__name {
    font-family: "Montserrat", Arial, sans-serif;
    font-weight: 700;
    font-size: 24px;
    letter-spacing: .5px;
    color: var(--brand-blue);
    line-height: 1;
  }
  .holder__role { font-size: 17px; font-weight: 400; color: var(--ink-grey); margin-top: 4px; }

  .contact {
    position: absolute;
    left: 40px; top: 206px;
    color: var(--paper);
    font-size: 15px;
    line-height: 20px;
    list-style: none;
  }
  .contact__address { margin-bottom: 6px; }
  .contact__item { display: flex; align-items: center; gap: 12px; }
  .contact__icon { width: 13px; height: 13px; flex: none; fill: var(--paper); }
</style>
</head>
<body>

<section class="card card--front" aria-label="Card front">
  <svg class="front-facet" viewBox="0 0 680 388" preserveAspectRatio="none" aria-hidden="true">
    <polygon points="600,0 680,0 680,388 150,388" fill="var(--brand-blue-light)"/>
  </svg>
  <div class="wordmark"><span class="wordmark__square"></span>K &amp; D A/C Compressors</div>
</section>

<section class="card card--back" aria-label="Card back">
  <div class="back-band"></div>

  <div class="holder">
    <p class="holder__name">MR. DANIEL</p>
    <p class="holder__role">Creative GM</p>
  </div>

  <div class="wordmark"><span class="wordmark__square"></span>K &amp; D A/C Compressors</div>

  <ul class="contact">
    <li class="contact__address">48207 Southwest 36th Street,<br>Palmetto Grove, Florida 33990</li>
    <li class="contact__item">
      <svg class="contact__icon" viewBox="0 0 16 16" aria-label="Phone"><path d="M3.5 1 6 1.5 7 5 5.3 6.3a9 9 0 0 0 4.4 4.4L11 9l3.5 1 .5 2.5-2 2C6.5 14.5 1.5 9.5 1.5 3z"/></svg>
      <span>305-472-1390</span>
    </li>
    <li class="contact__item">
      <svg class="contact__icon" viewBox="0 0 16 16" aria-label="Fax"><path d="M4 1h8v4H4zM1 6h14v6h-3v3H4v-3H1zm4 5v3h6v-3z"/></svg>
      <span>305-472-1391</span>
    </li>
    <li class="contact__item">
      <svg class="contact__icon" viewBox="0 0 16 16" aria-label="Website"><path d="M8 1a7 7 0 1 0 0 14A7 7 0 0 0 8 1zm0 1.5c.9 1 1.5 2.6 1.7 4.5H6.3C6.5 5.1 7.1 3.5 8 2.5zM2.6 7h2.2c.1-1.700.5-3.2 1.2-4.2A5.5 5.5 0 0 0 2.6 7zm8.6 0h2.2A5.5 5.5 0 0 0 10 2.8c.7 1 1.1 2.5 1.2 4.2zM2.6 9A5.5 5.5 0 0 0 6 13.2c-.7-1-1.1-2.5-1.2-4.2zm3.7 0c.2 1.9.8 3.5 1.7 4.5.9-1 1.5-2.600 1.7-4.5zm4.9 0c-.1 1.7-.5 3.2-1.2 4.2A5.5 5.5 0 0 0 13.4 9z"/></svg>
      <span>www.kdcoolunits.example</span>
    </li>
    <li class="contact__item">
      <svg class="contact__icon" viewBox="0 0 16 16" aria-label="Email"><path d="M1 3h14v10H1zm1.5 1.5v.3L8 8.6l5.5-3.8v-.3zm0 2.1v4.9h11V6.6L8 10.4z"/></svg>
      <span>support@kdcoolunits.example</span>
    </li>
  </ul>
</section>

</body>
</html>
```